Business Card for Language School (2 locations)

We need a sleek business card for a language school that is looking to update our image to be more professional. We work with students ages Pre-Kindergarten through adults. Our idea is to have an all-black business card with white or silver lettering. On the front will be the name of our school (Bright Maple English Academy), and on the back there will be information for our location, phone number, email, and website (and possibly social media information). We have two school branches, so the address, phone number, and email address will be different for each branch, but all of the other information will stay the same. We'd like each branch to have a different color card edge that is neon. We are also open to suggestions and new ideas!

Some answers to questions we have received:
1. The reason we haven't added a logo is because we are looking to get a new one. We hadn't originally planned to do that at this time, but we are going to look into updating our project to include that as another aspect of it. We had previously planned to just include the school name on the front without a logo at this time.
2. We currently have two branches of our school, and we want our business card design to be uniform for each location. While it might make sense to put the information on one card right now, we plan to have more locations in the future, so we want to plan ahead with a unified design right now.
3. Our school addresses and phone numbers can be found on our website: www.brightmapleenglish.example (at the bottom of the page)!
Updates

Part of this contest is also a new logo design. Our previous design was a train, which we would be open to keeping if it had an updated, sleeker design.

Contact Information for Business Card

Card #1:
Bright Maple English Academy (Qiaolin Branch)
Yuqing W. Rd. Sec. 3, Lane 412, No. 29, 1F
Beitou District, Taipei City 11268
02-2649-3058
qiaolin@brightmapleenglish.example

Card #2:
Bright Maple English Academy (Fenghe Branch)
Fulan Road, No. 318, 1F
Songshan District, Taipei City 10573
02-2761-4402
fenghe@brightmapleenglish.example

Both cards:
Website: www.brightmapleenglish.example
Facebook: www.facebook.com/brightmapleenglish
Instagram: @brightmapleenglish

```html
<!DOCTYPE html>
<html lang="en">
<head>
<meta charset="UTF-8">
<title>Bright Maple English Academy – Business Card Concepts</title>
<link href="https://fonts.googleapis.com/css2?family=Bebas+Neue&family=Arimo:wght@700&display=swap" rel="stylesheet">
<style>
  :root {
    --page: #ffffff;
    --card-edge: #0b0a0a;
    --card-mid: #26201d;
    --ink: #ffffff;
    --cap-grey: #e6e6e6;
    --branch-red: #fb0000;
    --branch-orange: #e5781c;
    --letters: rgba(120, 110, 104, 0.35);
  }
  * { box-sizing: border-box; margin: 0; padding: 0; }
  html, body { width: 1200px; height: 1200px; overflow: hidden; background: var(--page); }
  .sheet { position: relative; width: 1200px; height: 1200px; }

  .card {
    position: absolute;
    width: 570px;
    height: 350px;
    overflow: hidden;
    background: linear-gradient(180deg, var(--card-edge) 0%, var(--card-mid) 30%, var(--card-mid) 62%, var(--card-edge) 100%);
    font-family: "Arimo", Arial, sans-serif;
    font-weight: 700;
    color: var(--ink);
  }
  .card--front-a { left: 0; top: 208px; }
  .card--front-b { left: 631px; top: 208px; }
  .card--back-a { left: 0; top: 629px; }
  .card--back-b { left: 631px; top: 629px; }

  .letter-scatter {
    position: absolute;
    left: 0; right: 0;
    background: radial-gradient(ellipse at 50% 50%, var(--letters) 0%, rgba(120,110,104,0.12) 55%, rgba(0,0,0,0) 80%);
  }
  .card--front-a .letter-scatter, .card--front-b .letter-scatter { top: 262px; height: 88px; }
  .card--back-a .letter-scatter, .card--back-b .letter-scatter { top: 0; height: 95px; }

  .wordmark {
    position: absolute;
    left: 0; right: 0;
    text-align: center;
    font-family: "Bebas Neue", Impact, sans-serif;
    font-weight: 400;
    color: var(--ink);
    line-height: 0.9;
  }
  .card--front-a .wordmark { top: 112px; }
  .card--front-b .wordmark { top: 105px; }
  .wordmark__main { display: block; font-size: 96px; letter-spacing: 1px; }
  .wordmark__sub { display: block; font-size: 34px; letter-spacing: 2px; margin-top: 10px; }

  .back-name {
    position: absolute;
    left: 0; right: 0;
    top: 62px;
    text-align: center;
    font-family: "Bebas Neue", Impact, sans-serif;
    font-weight: 400;
    font-size: 34px;
    line-height: 1;
    color: var(--cap-grey);
    letter-spacing: 1px;
  }
  .back-name__dot {
    display: inline-block;
    width: 8px; height: 8px;
    border-radius: 50%;
    background: var(--cap-grey);
    margin-right: 10px;
    vertical-align: middle;
    position: relative; top: -3px;
  }

  .branch { position: absolute; font-size: 14.5px; line-height: 16.8px; color: var(--ink); }
  .branch--pill-left {
    left: 0; top: 179px; width: 275px; height: 104px;
    background: var(--branch-red);
    border-radius: 0 38px 38px 0;
    padding: 19px 0 0 22px;
  }
  .branch--pill-right {
    left: 295px; top: 179px; width: 275px; height: 104px;
    background: var(--branch-orange);
    border-radius: 38px 0 0 38px;
    padding: 19px 22px 0 0;
    text-align: right;
  }
  .branch--band {
    left: 0; width: 570px; height: 64px;
    text-align: center;
    padding-top: 14px;
  }
  .branch--band-red { top: 159px; background: var(--branch-red); }
  .branch--band-orange { top: 231px; background: var(--branch-orange); }

  .card__footer-band {
    position: absolute; left: 0; right: 0; bottom: 0; height: 67px;
    background: var(--card-edge);
  }
  .card--back-b .card__footer-band { height: 55px; }

  .web-links {
    position: absolute;
    left: 57px; top: 301px;
    width: 456px; height: 28px;
    border: 2px dashed var(--ink);
    font-size: 14.5px;
    line-height: 24px;
    text-align: center;
    white-space: nowrap;
  }
</style>
</head>
<body>
<main class="sheet">

  <section class="card card--front-a" aria-label="Card front, option A">
    <div class="letter-scatter" role="img" aria-label="Scattered faint alphabet letters decoration"></div>
    <h1 class="wordmark">
      <span class="wordmark__main">Bright Maple</span>
      <span class="wordmark__sub">English Academy</span>
    </h1>
  </section>

  <section class="card card--front-b" aria-label="Card front, option B">
    <div class="letter-scatter" role="img" aria-label="Scattered faint alphabet letters decoration"></div>
    <h1 class="wordmark">
      <span class="wordmark__main">Bright Maple</span>
      <span class="wordmark__sub">English Academy</span>
    </h1>
  </section>

  <section class="card card--back-a" aria-label="Card back, option A">
    <div class="letter-scatter" role="img" aria-label="Scattered faint alphabet letters decoration"></div>
    <p class="back-name"><span class="back-name__dot"></span>Bright Maple English Academy</p>
    <div class="card__footer-band"></div>
    <p class="branch branch--pill-left">1st branch or headquarters<br>address,<br>phone number,<br>and email address</p>
    <p class="branch branch--pill-right">2nd branch<br>address,<br>phone number,<br>and email address</p>
    <p class="web-links">website, and social media accounts (social pages and profiles)</p>
  </section>

  <section class="card card--back-b" aria-label="Card back, option B">
    <div class="letter-scatter" role="img" aria-label="Scattered faint alphabet letters decoration"></div>
    <p class="back-name"><span class="back-name__dot"></span>Bright Maple English Academy</p>
    <div class="card__footer-band"></div>
    <p class="branch branch--band branch--band-red">1st branch or headquarters<br>address, phone number, and email address</p>
    <p class="branch branch--band branch--band-orange">2nd branch<br>address,&nbsp; phone number, and email address</p>
    <p class="web-links">website, and social media accounts (social pages and profiles)</p>
  </section>

</main>
</body>
</html>
```